We need a label design for our new company called Marrow Finch.
We are a company that is producing Pet Supplements, but the first products launched are going to be for the dogs.
First 3 products that we are launching are:
-Multivitamin (12 in 1)
-Probiotic
-Hip and Joint
We need label design for this three products that are going to be packed in the black plastic jar with the count of 120 pieces in each.
I am uploading our logo, but please do not pay attention to the colors of the logo as that can be changed and adjusted.
- Label dimensions are 2.25" x 11.125"
-Corner radius 0.125

Attached some badges with registrations and approvals.

```html
<!DOCTYPE html>
<html lang="en">
<head>
<meta charset="utf-8">
<title>Marrow Finch Pet Supplement Labels</title>
<link href="https://fonts.googleapis.com/css2?family=Anton&family=Oswald:wght@500;600&family=Montserrat:wght@500;700;800&display=swap" rel="stylesheet">
<style>
  :root {
    --ink: #0d0d0d;
    --white: #ffffff;
    --paper: #ffffff;
    --green: #8cc63f;
    --orange: #f7941d;
    --red: #ed1c24;
    --badge-blue: #1f3f8f;
    --badge-ring: #d9dfeb;
    --fur-light: #c8873f;
    --fur-dark: #5a3418;
    --cat-light: #e9e9e6;
  }
  * { box-sizing: border-box; margin: 0; padding: 0; }
  html, body { width: 800px; height: 1200px; overflow: hidden; background: var(--paper); }
  .sheet {
    width: 800px; height: 1200px;
    display: flex; flex-direction: column; justify-content: center; align-items: center;
    gap: 38px;
  }
  .label {
    position: relative; width: 742px; height: 202px;
    background: var(--ink); border-radius: 4px; overflow: hidden;
    font-family: "Montserrat", sans-serif; color: var(--white);
  }
  .label--probiotic { --accent: var(--green); }
  .label--joint { --accent: var(--orange); }
  .label--multi { --accent: var(--red); }

  .label__top-band { position: absolute; left: 0; top: 0; width: 100%; height: 39px; background: var(--accent); }
  .label__bottom-band {
    position: absolute; left: 0; bottom: 0; width: 100%; height: 30px; background: var(--accent);
    display: flex; align-items: center; justify-content: center;
    font-weight: 800; font-size: 16px; letter-spacing: 3.2px;
  }
  .brand {
    position: absolute; left: 262px; top: 10px;
    display: flex; align-items: center; gap: 9px;
  }
  .brand__dot { width: 30px; height: 30px; border-radius: 50%; background: var(--white); }
  .brand__name { font-weight: 800; font-size: 19px; letter-spacing: 0.2px; color: var(--white); }

  .serving {
    position: absolute; left: 34px; top: 76px; width: 111px;
    border: 1.5px solid var(--white); padding: 2px 4px 3px;
    font-size: 6.3px; font-weight: 700; line-height: 1.3;
  }
  .serving__title {
    font-size: 9.5px; font-weight: 700; letter-spacing: 2.4px;
    border-bottom: 1.5px solid var(--white); margin: 0 -4px 2px; padding: 0 4px 1px;
  }
  .serving table { width: 100%; border-collapse: collapse; }
  .serving th { text-align: left; font-weight: 700; padding-bottom: 1px; border-bottom: 1px solid var(--white); }
  .serving td:first-child, .serving th:first-child { border-right: 1px solid var(--white); width: 52%; }
  .serving th:last-child { padding-left: 3px; }
  .serving td:last-child { padding-left: 18px; }

  .pets-photo {
    position: absolute; left: 163px; top: 70px; width: 144px; height: 102px;
    background: radial-gradient(ellipse at 30% 40%, var(--fur-light), var(--fur-dark) 60%, transparent 75%),
                radial-gradient(ellipse at 78% 70%, var(--cat-light), transparent 55%);
  }

  .title {
    position: absolute; top: 58px; font-family: "Anton", sans-serif; font-weight: 400;
    font-size: 56px; line-height: 1; letter-spacing: 0;
    color: var(--accent); white-space: nowrap; transform-origin: left top;
  }
  .title--probiotic { left: 257px; transform: scaleX(0.98); }
  .title--joint { left: 257px; transform: scaleX(0.88); }
  .title--joint .title__and { font-size: 30px; margin: 0 6px; }
  .title--multi { left: 255px; top: 62px; font-size: 52px; transform: scaleX(0.78); }
  .title__count {
    position: absolute; left: 443px; top: 112px; font-family: "Oswald", sans-serif;
    font-size: 8px; color: var(--accent);
  }
  .tagline {
    position: absolute; text-align: right; font-family: "Oswald", sans-serif; font-weight: 600;
    font-size: 14px; line-height: 1.3; text-transform: uppercase; letter-spacing: -0.3px;
  }
  .tagline--probiotic { right: 279px; top: 128px; }
  .tagline--joint { right: 271px; top: 128px; }
  .tagline--multi { right: 259px; top: 128px; }

  .badges { position: absolute; top: 46px; display: flex; flex-direction: column; gap: 9px; }
  .badges--left { left: 483px; }
  .badges--right { left: 503px; }
  .badge { width: 33px; height: 33px; border-radius: 50%; background: var(--badge-blue); border: 3px solid var(--badge-ring); }

  .blurb {
    position: absolute; left: 545px; top: 46px; width: 168px;
    font-size: 6.9px; font-weight: 500; line-height: 1.3;
  }
  .member-badge { position: absolute; left: 545px; top: 132px; width: 43px; height: 29px; background: var(--white); }
</style>
</head>
<body>
<main class="sheet">

  <section class="label label--probiotic">
    <div class="label__top-band"></div>
    <div class="brand"><span class="brand__dot"></span><span class="brand__name">MARROW FINCH</span></div>
    <div class="serving">
      <div class="serving__title">SERVING SIZE</div>
      <table>
        <tr><th>Body Weight</th><th>Chews / Day</th></tr>
        <tr><td>Under 10 lbs</td><td>1</td></tr>
        <tr><td>10-30 lbs</td><td>2</td></tr>
        <tr><td>31-60 lbs</td><td>3</td></tr>
        <tr><td>61-90 lbs</td><td>4</td></tr>
        <tr><td>over 90lbs</td><td>5</td></tr>
      </table>
    </div>
    <div class="pets-photo" role="img" aria-label="Photo of a golden retriever beside a white cat"></div>
    <h2 class="title title--probiotic">PROBIOTIC</h2>
    <p class="tagline tagline--probiotic">Digestive Health<br>For Cats and Dogs</p>
    <div class="badges badges--left">
      <span class="badge" role="img" aria-label="Natural and organic ingredients badge"></span>
      <span class="badge" role="img" aria-label="Made in USA badge"></span>
      <span class="badge" role="img" aria-label="Registered facility badge"></span>
    </div>
    <p class="blurb">Give your furry friend the gift of a balanced and thriving digestive system with our premium Probiotic for Pets. Specially formulated to support digestive health in cats, dogs, and other beloved pets, our carefully selected probiotic strains are perfect for pets of all sizes and ages.</p>
    <div class="member-badge" role="img" aria-label="Trade association member badge"></div>
    <div class="label__bottom-band">PET SUPPLEMENT</div>
  </section>

  <section class="label label--joint">
    <div class="label__top-band"></div>
    <div class="brand"><span class="brand__dot"></span><span class="brand__name">MARROW FINCH</span></div>
    <div class="serving">
      <div class="serving__title">SERVING SIZE</div>
      <table>
        <tr><th>Body Weight</th><th>Chews / Day</th></tr>
        <tr><td>Under 10 lbs</td><td>1</td></tr>
        <tr><td>10-30 lbs</td><td>2</td></tr>
        <tr><td>31-60 lbs</td><td>3</td></tr>
        <tr><td>61-90 lbs</td><td>4</td></tr>
        <tr><td>over 90lbs</td><td>5</td></tr>
      </table>
    </div>
    <div class="pets-photo" role="img" aria-label="Photo of a golden retriever beside a white cat"></div>
    <h2 class="title title--joint">HIP<span class="title__and">AND</span>JOINT</h2>
    <p class="tagline tagline--joint">Helping your pet move<br>with ease and comfort!</p>
    <div class="badges badges--left">
      <span class="badge" role="img" aria-label="Natural and organic ingredients badge"></span>
      <span class="badge" role="img" aria-label="Made in USA badge"></span>
      <span class="badge" role="img" aria-label="Registered facility badge"></span>
    </div>
    <p class="blurb">Give your four-legged friend the gift of mobility and comfort with our premium Hip and Joint Support for Pets. Specially formulated to promote joint health and alleviate discomfort, our carefully crafted blend of ingredients is perfect for cats, dogs, and other furry companions of all sizes and ages.</p>
    <div class="member-badge" role="img" aria-label="Trade association member badge"></div>
    <div class="label__bottom-band">PET SUPPLEMENT</div>
  </section>

  <section class="label label--multi">
    <div class="label__top-band"></div>
    <div class="brand"><span class="brand__dot"></span><span class="brand__name">MARROW FINCH</span></div>
    <div class="serving">
      <div class="serving__title">SERVING SIZE</div>
      <table>
        <tr><th>Body Weight</th><th>Chews / Day</th></tr>
        <tr><td>Under 10 lbs</td><td>1</td></tr>
        <tr><td>10-30 lbs</td><td>2</td></tr>
        <tr><td>31-60 lbs</td><td>3</td></tr>
        <tr><td>61-90 lbs</td><td>4</td></tr>
        <tr><td>over 90lbs</td><td>5</td></tr>
      </table>
    </div>
    <div class="pets-photo" role="img" aria-label="Photo of a golden retriever beside a white cat"></div>
    <h2 class="title title--multi">MULTIVITAMIN</h2>
    <span class="title__count">(12 IN 1)</span>
    <p class="tagline tagline--multi">Boost your pet's immunity<br>lustrous coat and healthy skin</p>
    <div class="badges badges--right">
      <span class="badge" role="img" aria-label="Natural and organic ingredients badge"></span>
      <span class="badge" role="img" aria-label="Made in USA badge"></span>
      <span class="badge" role="img" aria-label="Registered facility badge"></span>
    </div>
    <p class="blurb">Specially formulated to support the well-being of cats and dogs and small animals, our comprehensive blend of essential vitamins and minerals is the perfect addition to your pet's daily routine.</p>
    <div class="member-badge" role="img" aria-label="Trade association member badge"></div>
    <div class="label__bottom-band">PET SUPPLEMENT</div>
  </section>

</main>
</body>
</html>
```